Waterproofing Adhesive company needs design for bucket

We need a design for our 20kg/15kg and 4 kg bucket, Our companys name is Tolvarex Co LLC based in Umm Al Quwain, United Arab Emirates . Our main business is into waterproofing paint and Adhesive manufacturing. We are looking for a creative design for our buckets and paper bags. The design have to be attractive, The color theme of our company is light orange and yellow. I have attached the company logo along with this.

Target Market(s)

B2b , construction companys
Maintenance company

Industry/Entity Type

Manufacturer

Requirements
Must have
• It must have the company logo
• a spcae in centre to write the different products names
Nice to have
• A attractive design for placing the bucket in retail shops

```html
<!DOCTYPE html>
<html lang="en">
<head>
<meta charset="utf-8">
<title>Tolvarex Co LLC – Waterproofing Bucket Label</title>
<link rel="stylesheet" href="https://fonts.googleapis.com/css2?family=Roboto:ital,wght@0,700;0,900;1,900&family=Roboto+Condensed:wght@400;700&display=swap">
<style>
  :root {
    --white: #ffffff;
    --pattern-tone: #f6f4f1;
    --yellow-light: #ffe733;
    --yellow-mid: #ffd21a;
    --yellow-deep: #fbb515;
    --orange: #ea8a14;
    --orange-brand: #e36d1c;
    --rust: #c44a12;
    --ink: #3a2a10;
  }
  * { box-sizing: border-box; margin: 0; padding: 0; }
  html, body { width: 1200px; height: 1200px; overflow: hidden; background: var(--white); }
  .label {
    position: relative;
    width: 1200px;
    height: 1200px;
    background: var(--white);
    font-family: "Roboto", Arial, sans-serif;
  }
  .label__pattern {
    position: absolute;
    inset: 0;
    background: var(--pattern-tone);
  }
  .label__paint {
    position: absolute;
    left: 0;
    top: 500px;
    width: 1200px;
    height: 640px;
  }
  .brand {
    position: absolute;
    top: 250px;
    left: 0;
    width: 1200px;
    display: flex;
    justify-content: center;
    align-items: center;
    gap: 22px;
  }
  .brand__dot {
    width: 70px;
    height: 70px;
    border-radius: 50%;
    background: var(--orange-brand);
  }
  .brand__name {
    font-size: 64px;
    font-weight: 700;
    color: var(--orange-brand);
    letter-spacing: 0.5px;
  }
  .headline {
    position: absolute;
    top: 600px;
    left: 300px;
    width: 640px;
    font-weight: 900;
    font-style: italic;
    font-size: 92px;
    line-height: 98px;
    color: var(--rust);
    transform: rotate(-1deg);
  }
  .product-tag {
    position: absolute;
    top: 812px;
    left: 290px;
    width: 630px;
    height: 84px;
    background: var(--white);
    transform: skewX(-10deg) rotate(-1.5deg);
    box-shadow: 0 8px 0 var(--rust);
    display: flex;
    align-items: center;
    justify-content: center;
  }
  .product-tag__text {
    transform: skewX(10deg);
    font-weight: 900;
    font-style: italic;
    font-size: 60px;
    letter-spacing: 3px;
    color: var(--orange);
  }
  .features {
    position: absolute;
    top: 935px;
    left: 300px;
    width: 700px;
    display: grid;
    grid-template-columns: 1fr 1fr;
    column-gap: 30px;
    row-gap: 14px;
    list-style: none;
  }
  .features__item {
    display: flex;
    align-items: center;
    gap: 12px;
    font-family: "Roboto Condensed", Arial, sans-serif;
    font-size: 19px;
    color: var(--ink);
  }
  .features__tick { width: 22px; height: 22px; flex: none; }
  .net-weight {
    position: absolute;
    top: 1080px;
    left: 318px;
    color: var(--ink);
  }
  .net-weight__label {
    font-family: "Roboto Condensed", Arial, sans-serif;
    font-weight: 700;
    font-size: 18px;
  }
  .net-weight__value {
    font-weight: 900;
    font-size: 54px;
    line-height: 1;
    color: var(--orange);
  }
</style>
</head>
<body>
<main class="label">
  <div class="label__pattern" role="img" aria-label="Faint light grey decorative leaf pattern background"></div>

  <svg class="label__paint" viewBox="0 0 1200 640" role="img" aria-label="Bright yellow and orange painted brush-stroke band">
    <defs>
      <linearGradient id="paintGradient" x1="0" y1="0" x2="0" y2="1">
        <stop offset="0" stop-color="var(--yellow-mid)"/>
        <stop offset="0.5" stop-color="var(--yellow-deep)"/>
        <stop offset="1" stop-color="var(--yellow-light)"/>
      </linearGradient>
    </defs>
    <path d="M0 40 L120 20 L260 50 L420 30 L600 60 L780 40 L960 70 L1200 50 L1200 590 L1040 610 L860 585 L680 620 L500 595 L320 625 L160 600 L0 620 Z" fill="url(#paintGradient)"/>
  </svg>

  <div class="brand">
    <span class="brand__dot"></span>
    <span class="brand__name">Tolvarex Co LLC</span>
  </div>

  <h1 class="headline">LOREM IPSUM<br>DUMMY TEXT.</h1>

  <div class="product-tag"><span class="product-tag__text">WATERPROOFING</span></div>

  <ul class="features">
    <li class="features__item"><svg class="features__tick" viewBox="0 0 22 22"><path d="M3 11 L9 17 L20 4" fill="none" stroke="var(--orange-brand)" stroke-width="3.5"/></svg>Lorem Ipsum is simply dummy text.</li>
    <li class="features__item"><svg class="features__tick" viewBox="0 0 22 22"><path d="M3 11 L9 17 L20 4" fill="none" stroke="var(--orange-brand)" stroke-width="3.5"/></svg>Lorem Ipsum is simply dummy text.</li>
    <li class="features__item"><svg class="features__tick" viewBox="0 0 22 22"><path d="M3 11 L9 17 L20 4" fill="none" stroke="var(--orange-brand)" stroke-width="3.5"/></svg>Lorem Ipsum is simply dummy text.</li>
    <li class="features__item"><svg class="features__tick" viewBox="0 0 22 22"><path d="M3 11 L9 17 L20 4" fill="none" stroke="var(--orange-brand)" stroke-width="3.5"/></svg>Lorem Ipsum is simply dummy text.</li>
    <li class="features__item"><svg class="features__tick" viewBox="0 0 22 22"><path d="M3 11 L9 17 L20 4" fill="none" stroke="var(--orange-brand)" stroke-width="3.5"/></svg>Lorem Ipsum is simply dummy text.</li>
    <li class="features__item"><svg class="features__tick" viewBox="0 0 22 22"><path d="M3 11 L9 17 L20 4" fill="none" stroke="var(--orange-brand)" stroke-width="3.5"/></svg>Lorem Ipsum is simply dummy text.</li>
    <li class="features__item"><svg class="features__tick" viewBox="0 0 22 22"><path d="M3 11 L9 17 L20 4" fill="none" stroke="var(--orange-brand)" stroke-width="3.5"/></svg>Lorem Ipsum is simply dummy text.</li>
    <li class="features__item"><svg class="features__tick" viewBox="0 0 22 22"><path d="M3 11 L9 17 L20 4" fill="none" stroke="var(--orange-brand)" stroke-width="3.5"/></svg>Lorem Ipsum is simply dummy text.</li>
  </ul>

  <div class="net-weight">
    <div class="net-weight__label">Net Wt.</div>
    <div class="net-weight__value">20kg</div>
  </div>
</main>
</body>
</html>
```